Granite Peak Roofing & Exteriors Ltd

I would like to start a Facebook page for business that outlines granite peak roofing . We have been in business since 2005 & have completed more than 5000 projects . Our company is area licensed, insured , covered by qlf , ntz member , journey man roofers , offer financing, zero down payment required , free quotes , serving red deer & area .

Please do not put years on the homepage.

Target Market(s)

Roofers in red deer & central Alberta

Industry/Entity Type

Roofing

Requirements
Must have
• Shingles , soffit , fascia , siding , gutters , roof repair , exterior painting , exterior washing .

```html
<!DOCTYPE html>
<html lang="en">
<head>
<meta charset="utf-8">
<title>Granite Peak Roofing & Exteriors Ltd — Cover</title>
<link href="https://fonts.googleapis.com/css2?family=League+Gothic&display=swap" rel="stylesheet">
<style>
  :root {
    --stage: #0e3384;
    --paper: #ffffff;
    --brand-red: #c1121f;
    --ink: #0b0b0b;
    --badge-cream: #fbf7dc;
    --badge-blue: #1d5aa8;
    --badge-grey: #c9ccd3;
  }
  * { margin: 0; padding: 0; box-sizing: border-box; }
  html, body { width: 1200px; height: 900px; overflow: hidden; }
  body { background: var(--stage); position: relative; font-family: "League Gothic", "Arial Narrow", sans-serif; }

  .cover {
    position: absolute; left: 40px; top: 243px;
    width: 1120px; height: 414px;
    background: var(--paper); overflow: hidden;
  }
  .cover__collage { position: absolute; inset: 0; width: 100%; height: 100%; }

  .headline {
    position: absolute; left: 57px; top: 30px;
    color: var(--brand-red); font-size: 46px; line-height: 42px; font-weight: 400;
    text-transform: uppercase; letter-spacing: 1.6px; white-space: nowrap;
  }

  .services {
    position: absolute; left: 56px; top: 166px; list-style: none;
    display: grid; grid-template-columns: 104px 86px 106px auto;
    color: var(--ink); font-size: 23px; line-height: 24px;
  }
  .service { display: flex; align-items: center; gap: 3px; white-space: nowrap; }
  .service svg { width: 16px; height: 16px; flex: none; }

  .offer-bar {
    position: absolute; left: 54px; top: 223px; width: 441px; height: 31px;
    background: var(--brand-red); color: #fff;
    font-size: 21px; line-height: 31px; text-align: center; letter-spacing: 0.3px;
  }

  .service-area {
    position: absolute; left: 50px; top: 262px; font-weight: 400;
    color: var(--ink); font-size: 56px; line-height: 56px; letter-spacing: 0.3px; white-space: nowrap;
  }

  .credentials {
    position: absolute; left: 36px; top: 355px; width: 230px; height: 51px;
    background: var(--badge-cream); display: flex; align-items: center; gap: 10px; padding: 0 10px;
  }
  .credentials__badge { height: 30px; border-radius: 3px; }
  .credentials__badge--qlf { width: 120px; background: var(--badge-grey); border-radius: 14px; }
  .credentials__badge--ntz { width: 76px; height: 38px; background: var(--badge-blue); }

  .contact { position: absolute; left: 282px; top: 338px; }
  .contact__phone {
    display: flex; align-items: center; gap: 8px;
    color: var(--brand-red); font-size: 40px; line-height: 36px; letter-spacing: 0.5px;
  }
  .contact__phone svg { width: 34px; height: 34px; }
  .contact__web { display: flex; margin-top: 2px; height: 22px; font-size: 17px; line-height: 22px; color: #fff; }
  .contact__label { background: var(--brand-red); padding: 0 5px; }
  .contact__url { background: var(--ink); padding: 0 8px 0 12px; }
</style>
</head>
<body>
  <section class="cover" aria-label="Granite Peak Roofing & Exteriors Ltd cover banner">
    <svg class="cover__collage" viewBox="0 0 1400 518" preserveAspectRatio="none">
      <defs>
        <linearGradient id="tone-tan" x1="0" y1="0" x2="1" y2="1">
          <stop offset="0" stop-color="#3f7fd6"/><stop offset="0.45" stop-color="#c9b49a"/><stop offset="1" stop-color="#5a5148"/>
        </linearGradient>
        <linearGradient id="tone-stone" x1="0" y1="0" x2="0" y2="1">
          <stop offset="0" stop-color="#6f6d6a"/><stop offset="0.6" stop-color="#8a8680"/><stop offset="1" stop-color="#2d5fc4"/>
        </linearGradient>
        <linearGradient id="tone-red" x1="0" y1="0" x2="1" y2="1">
          <stop offset="0" stop-color="#b9cbe0"/><stop offset="0.45" stop-color="#7d8186"/><stop offset="1" stop-color="#8e2a2e"/>
        </linearGradient>
        <linearGradient id="tone-build" x1="0" y1="0" x2="0" y2="1">
          <stop offset="0" stop-color="#3a6ed8"/><stop offset="0.4" stop-color="#4a4650"/><stop offset="1" stop-color="#b6916a"/>
        </linearGradient>
      </defs>
      <polygon role="img" aria-label="Photo: two-storey tan house with work truck and trailer" fill="url(#tone-tan)" points="620,0 975,0 1040,75 855,255"/>
      <polygon role="img" aria-label="Photo: stone-faced house with new grey roof" fill="url(#tone-stone)" points="975,0 1400,0 1400,95 1215,280 1040,75"/>
      <polygon role="img" aria-label="Photo: red-sided house with freshly shingled roof" fill="url(#tone-red)" points="855,255 1040,75 1215,280 985,518"/>
      <polygon role="img" aria-label="Photo: new house under construction with roofing materials" fill="url(#tone-build)" points="985,518 1215,280 1400,95 1400,518"/>
      <g stroke="#fff" stroke-width="5">
        <line x1="855" y1="255" x2="1040" y2="75"/>
        <line x1="1040" y1="75" x2="1215" y2="280"/>
        <line x1="985" y1="518" x2="1400" y2="95"/>
      </g>
      <line x1="978" y1="518" x2="1000" y2="494" stroke="#c1121f" stroke-width="4"/>
    </svg>

    <h1 class="headline">We specialize in residential,<br>commercial &amp; industrial<br>roofing and exteriors</h1>

    <ul class="services">
      <li class="service"><svg viewBox="0 0 16 16"><circle cx="8" cy="8" r="6.5" fill="none" stroke="#c1121f" stroke-width="1.5"/><path d="M4.5 8.2l2.4 2.4L13.5 3" fill="none" stroke="#c1121f" stroke-width="1.8"/></svg>Shingles</li>
      <li class="service"><svg viewBox="0 0 16 16"><circle cx="8" cy="8" r="6.5" fill="none" stroke="#c1121f" stroke-width="1.5"/><path d="M4.5 8.2l2.4 2.4L13.5 3" fill="none" stroke="#c1121f" stroke-width="1.8"/></svg>Fascia</li>
      <li class="service"><svg viewBox="0 0 16 16"><circle cx="8" cy="8" r="6.5" fill="none" stroke="#c1121f" stroke-width="1.5"/><path d="M4.5 8.2l2.4 2.4L13.5 3" fill="none" stroke="#c1121f" stroke-width="1.8"/></svg>Gutters</li>
      <li class="service"><svg viewBox="0 0 16 16"><circle cx="8" cy="8" r="6.5" fill="none" stroke="#c1121f" stroke-width="1.5"/><path d="M4.5 8.2l2.4 2.4L13.5 3" fill="none" stroke="#c1121f" stroke-width="1.8"/></svg>Exterior painting</li>
      <li class="service"><svg viewBox="0 0 16 16"><circle cx="8" cy="8" r="6.5" fill="none" stroke="#c1121f" stroke-width="1.5"/><path d="M4.5 8.2l2.4 2.4L13.5 3" fill="none" stroke="#c1121f" stroke-width="1.8"/></svg>Soffit</li>
      <li class="service"><svg viewBox="0 0 16 16"><circle cx="8" cy="8" r="6.5" fill="none" stroke="#c1121f" stroke-width="1.5"/><path d="M4.5 8.2l2.4 2.4L13.5 3" fill="none" stroke="#c1121f" stroke-width="1.8"/></svg>Siding</li>
      <li class="service"><svg viewBox="0 0 16 16"><circle cx="8" cy="8" r="6.5" fill="none" stroke="#c1121f" stroke-width="1.5"/><path d="M4.5 8.2l2.4 2.4L13.5 3" fill="none" stroke="#c1121f" stroke-width="1.8"/></svg>Roof repair</li>
      <li class="service"><svg viewBox="0 0 16 16"><circle cx="8" cy="8" r="6.5" fill="none" stroke="#c1121f" stroke-width="1.5"/><path d="M4.5 8.2l2.4 2.4L13.5 3" fill="none" stroke="#c1121f" stroke-width="1.8"/></svg>Exterior washing</li>
    </ul>

    <p class="offer-bar">FINANCING, ZERO DOWN PAYMENT REQUIRED , FREE QUOTES</p>

    <h2 class="service-area">SERVING RED DEER &amp; AREA</h2>

    <div class="credentials" aria-label="Membership badges">
      <span class="credentials__badge credentials__badge--qlf"></span>
      <span class="credentials__badge credentials__badge--ntz"></span>
    </div>

    <div class="contact">
      <p class="contact__phone">
        <svg viewBox="0 0 34 34"><circle cx="17" cy="17" r="15" fill="none" stroke="#c1121f" stroke-width="2.5"/><path d="M11 9c1.5-1 2.5-.8 3.2.6l1.3 2.6c.5 1 .2 1.8-.7 2.4l-1 .7c.9 2.3 2.6 4.1 4.9 5.1l.7-1c.6-.9 1.5-1.1 2.4-.6l2.6 1.4c1.3.7 1.4 1.8.4 3.2-1.2 1.6-3 2.2-5 1.5-4.5-1.6-8-5.2-9.5-9.8-.6-2 .1-4 .7-5.1z" fill="#c1121f"/></svg>
        403. 555. 0187
      </p>
      <p class="contact__web"><span class="contact__label">Our Website</span><span class="contact__url">www.granitepeakroofing.ca</span></p>
    </div>
  </section>
</body>
</html>
```